design an app for runners to engage them in collective challenges

Creative Brief: Running Application - Collective Challenges
Objective
To design a simple yet impactful mobile application for runners, centered around collective challenges. The app should offer an engaging, user-friendly experience while encouraging participation in running challenges. Starting with a minimalist and robust version, the design must focus on essential features, allowing for future enhancements as the user base grows.

Target Audience
Primary Users: Casual to dedicated runners who enjoy tracking their progress and participating in challenges.
Motivations: Community-driven goals, personal achievements, and tangible rewards.
Needs: A visually appealing, straightforward interface with real-time progress tracking and clear challenge objectives.
Core Features
Main Screen: Current Challenge

Displays the active challenge with a title, visual, prize description, and countdown for kilometers remaining.
Prominent “Join” button for easy participation.
Quick access to challenge conditions (eg, most kilometers, fastest pace, random draw).
Challenge Details

Includes challenge rules, detailed prize information, and victory conditions.
Simplified text for clarity and engagement.
Past Challenges

Showcases previous challenges, total kilometers achieved, and winners.
Admin Section

Enables challenge creation with scheduling, descriptions, and victory criteria.
Minimalist design for ease of use.
Look and Feel
Visual Identity: Clean, modern, and energetic design reflecting the spirit of running and collective achievement.
Color Palette:
Vibrant primary colors: Blue and green for energy and motivation.
Accent colors: Orange or yellow for highlights, paired with a dark background for strong contrast.
Typography:
Sans-serif fonts like Lato or Montserrat for readability.
Bold, prominent numbers for key statistics like kilometers completed.
Icons and Graphics:
Minimalistic icons with light, functional animations (eg, a moving kilometer counter).
Clear, motivational visuals to support collective progress.
Tone and Style
Tone: Encouraging, community-focused, and goal-oriented.
Style: Minimalistic with a focus on clarity and user engagement.
References
Inspirations:
Velta Stride Circle for its simplicity and modern interface.
Quorvo for its community features and tracking precision.
Deliverables
Wireframes and UI designs for all key screens: login, current challenge, challenge details, past challenges, and admin panel.
Visual assets: icons, buttons, and animations.
A consistent design system to ensure scalability for future features.
Updates

Target Market(s)

Casual to dedicated runners who enjoy tracking their progress and participating in challenges.

Industry/Entity Type

sport

Font styles to use
Sans Serif

Colors

Designer to choose colors to be used in the design.

Requirements
Must have
• to design all screens

```html
<!DOCTYPE html>
<html lang="en">
<head>
<meta charset="utf-8">
<title>Runvex – Collective Challenges</title>
<link rel="stylesheet" href="https://fonts.googleapis.com/css2?family=Montserrat:wght@400;500;600;700&display=swap">
<style>
:root{
  --canvas:#2b2f37;
  --screen:#121a2b;
  --header:#0f1524;
  --card:#1b2437;
  --card-blue:#1e3468;
  --input:#242d3e;
  --line:#3a4458;
  --blue:#2f66ea;
  --blue-deep:#1b45b8;
  --gold:#d9a21b;
  --bronze:#c27a2a;
  --green:#27c763;
  --text:#ffffff;
  --muted:#8e97aa;
  --track:#e9ecf2;
}
*{box-sizing:border-box;margin:0;padding:0}
html,body{width:1200px;height:1200px;overflow:hidden}
body{background:var(--canvas);font-family:'Montserrat',sans-serif;color:var(--text);position:relative}
.screen{position:absolute;width:250px;height:530px;background:var(--screen);border-radius:30px;overflow:hidden;display:flex;flex-direction:column}
.s1{left:97px;top:40px}.s2{left:475px;top:40px}.s3{left:853px;top:40px}
.s4{left:97px;top:630px}.s5{left:475px;top:630px}.s6{left:853px;top:630px}

.app-header{background:var(--header);padding:36px 14px 12px;display:flex;align-items:center;gap:7px}
.avatar{width:28px;height:28px;border-radius:50%;background:var(--blue);display:flex;align-items:center;justify-content:center;font-weight:700;font-size:9px}
.greet small{display:block;font-size:7px;color:#c7cdd8}
.greet strong{font-size:9px;font-weight:600}
.bell{margin-left:auto}
.body{padding:10px 12px 0;flex:1;display:flex;flex-direction:column;gap:7px}
.label{font-size:9px;font-weight:500;margin:3px 0 0 10px}

.hero{background:linear-gradient(160deg,#2c64ec,#1c45bd);border-radius:6px;padding:10px 12px;position:relative}
.hero .crown{position:absolute;right:10px;top:9px}
.hero .cap{font-size:8.5px;color:#cdd8f7}
.hero .big{font-size:18px;font-weight:700;margin:1px 0 8px}
.stats{display:flex;justify-content:space-between;font-size:8.5px}
.stats span{display:block;color:#cdd8f7}
.stats b{font-weight:500}
.stats .c{text-align:center}

.challenge{background:var(--card);border-radius:6px;padding:10px 12px}
.pill{display:inline-block;background:#243a70;color:#7ea2ff;font-size:8px;padding:3px 8px;border-radius:8px}
.ch-title{font-size:9.5px;font-weight:600;margin-top:6px}
.ch-sub{font-size:6.5px;color:var(--muted);margin-top:1px}
.prog-row{display:flex;justify-content:space-between;font-size:6.5px;color:var(--muted);margin-top:8px}
.bar{height:4px;background:var(--track);border-radius:2px;margin-top:2px;overflow:hidden}
.bar i{display:block;height:100%;width:56%;background:var(--blue)}
.prize{display:flex;align-items:center;gap:7px;background:var(--blue-deep);border-radius:4px;padding:8px 10px;margin-top:9px;font-size:9px}
.prize b{margin-left:auto;font-weight:700}

.activity{background:var(--card);border-radius:4px;padding:5px 10px;display:flex;align-items:center}
.activity strong{font-size:9px;font-weight:600;display:block}
.activity small{font-size:6.5px;color:var(--muted)}
.activity svg{margin-left:auto}

.past{background:var(--card-blue);border-radius:4px;padding:7px 12px;display:flex;align-items:center}
.past strong{font-size:9px;font-weight:600;display:block}
.past small{font-size:6.5px;color:var(--muted);display:block;margin-top:1px}
.past .end{margin-left:auto;display:flex;flex-direction:column;align-items:center;gap:8px}

.btn{background:linear-gradient(180deg,#2f66ea,#1f48c2);border-radius:6px;height:40px;display:flex;align-items:center;justify-content:center;font-size:9.5px;font-weight:500}
.tabbar{display:flex;justify-content:space-around;padding:14px 20px 22px;margin-top:auto}

.form{padding:0 14px}
.form label{display:block;font-size:9px;font-weight:600;margin:10px 0 5px}
.field{height:31px;border:1px solid var(--line);background:var(--input);border-radius:5px;padding:0 10px;display:flex;align-items:center;font-size:8.5px;color:var(--muted)}

.brand{display:flex;flex-direction:column;align-items:center;padding-top:74px}
.brand-mark{display:flex;align-items:center;gap:6px;font-size:13px;font-weight:600}
.brand-mark i{width:14px;height:14px;background:var(--blue);border-radius:3px}
.brand h1{font-size:12px;font-weight:600;margin-top:10px}
.brand p{font-size:6.5px;margin-top:9px;color:#dfe3ea}

.topbar{background:var(--header);padding:36px 14px 12px;display:flex;align-items:center;gap:8px;font-size:10px;font-weight:500}
.save{margin-left:auto;background:var(--blue);border-radius:5px;padding:7px 18px;font-size:9.5px}
.detail-hero{background:linear-gradient(180deg,#1d3f9a,#121a2b);padding:8px 16px 14px}
.live{font-size:9px;color:var(--green);display:flex;align-items:center;gap:5px}
.live i{width:9px;height:9px;border-radius:50%;background:var(--green)}
.detail-hero h2{font-size:12px;font-weight:600;margin-top:3px}
.tiles{display:flex;gap:6px;padding:0 6px}
.tile{flex:1;background:var(--card);border-radius:3px;padding:6px 0;text-align:center;font-size:8px;color:#c6ccd8}
.tile b{display:block;color:var(--text);font-size:11px;font-weight:600;margin-top:2px}
.panel{background:var(--card);margin:6px 6px 0;border-radius:4px;padding:8px 12px}
.panel h3{font-size:9.5px;font-weight:600}
.rules{display:flex;flex-direction:column;gap:6px}
.rule{display:flex;gap:10px;align-items:center}
.rule strong{font-size:9px;font-weight:500;display:block}
.rule small{font-size:7.5px;color:#cfd4de}
.sec{font-size:9.5px;font-weight:600;margin:9px 0 0 18px}
.places{margin:6px 6px 0;background:var(--card);border-radius:4px;padding:0 5px}
.place{display:flex;align-items:center;gap:8px;padding:5px 0;font-size:9.5px;border-bottom:1px solid #aeb5c2}
.place:last-child{border-bottom:none}
.place b{margin-left:auto;font-weight:500}
.dashed{height:66px;border:1px dashed var(--line);border-radius:5px;display:flex;flex-direction:column;align-items:center;justify-content:center;font-size:9px;color:var(--muted);font-weight:600}
.dashed small{font-size:7.5px;font-weight:400}
</style>
</head>
<body>

<!-- Sign up -->
<section class="screen s1">
  <div class="brand">
    <div class="brand-mark"><i></i>Runvex</div>
    <h1>Create Account</h1>
    <p>Join our running community and start tracking your progress</p>
  </div>
  <div class="form">
    <label>First Name</label><div class="field">Theo</div>
    <label>Last Name</label><div class="field">Marlow</div>
    <label>Email</label><div class="field">tm@runmail.app</div>
    <label>Password</label><div class="field">tm@runmail.app</div>
    <label>Address</label><div class="field">123</div>
  </div>
  <div class="btn" style="margin:42px 14px 0">Publish Challenge</div>
</section>

<!-- Home -->
<section class="screen s2">
  <header class="app-header">
    <div class="avatar">TM</div>
    <div class="greet"><small>Welcome Back</small><strong>Theo M.</strong></div>
    <svg class="bell" width="16" height="18" viewBox="0 0 16 18" fill="none" stroke="#cfd4de" stroke-width="1.4"><path d="M3 13V8a5 5 0 0110 0v5l1.5 2h-13z"/><path d="M6.5 16.5a1.6 1.6 0 003 0"/></svg>
  </header>
  <div class="body">
    <div class="hero">
      <svg class="crown" width="22" height="16" viewBox="0 0 22 16" fill="none" stroke="var(--gold)" stroke-width="1.6"><path d="M2 4l5 5 4-7 4 7 5-5-2 9H4z"/><path d="M4 15h14"/></svg>
      <div class="cap">Today's Progress</div>
      <div class="big">2.5 km</div>
      <div class="stats"><div><span>Time</span><b>22 Min</b></div><div><span>Pace</span><b>8'48" /km</b></div><div><span>Calories</span><b>186 kcal</b></div></div>
    </div>
    <div class="label">Current Challenge</div>
    <div class="challenge">
      <span class="pill">Active</span>
      <div class="ch-title">100km Challenge</div>
      <div class="ch-sub">12 days remaining</div>
      <div class="prog-row"><span>35.8 km completed</span><span>53%</span></div>
      <div class="bar"><i></i></div>
      <div class="prize"><svg width="13" height="14" viewBox="0 0 13 14" fill="none" stroke="#5c8bff" stroke-width="1.6"><path d="M2 1l4.5 6L11 1"/><circle cx="6.5" cy="9.5" r="3.2"/></svg>Prize Pool<b>US. 10,000</b></div>
    </div>
    <div class="label">Recent Activities</div>
    <div class="activity"><div><strong>Today • 6:30 AM</strong><small>2.5 km &nbsp;22 min</small></div><svg width="7" height="10" viewBox="0 0 7 10" fill="none" stroke="#fff" stroke-width="1.8"><path d="M1.5 1l4 4-4 4"/></svg></div>
    <div class="activity"><div><strong>Yesterday • 6:15 AM</strong><small>3.2 km &nbsp;28 min</small></div><svg width="7" height="10" viewBox="0 0 7 10" fill="none" stroke="#fff" stroke-width="1.8"><path d="M1.5 1l4 4-4 4"/></svg></div>
    <div class="btn" style="margin-top:4px">Start Run</div>
  </div>
  <nav class="tabbar">
    <svg width="14" height="13" viewBox="0 0 14 13" fill="var(--blue)"><path d="M7 1l6 5.5h-2V12H8.5V8.5h-3V12H3V6.5H1z"/></svg>
    <svg width="13" height="13" viewBox="0 0 13 13" fill="#9aa3b4"><path d="M3 1h7v4a3.5 3.5 0 01-7 0zM5.5 9h2v2h2v1.5h-6V11h2z"/><path d="M3 2H1v1.5a2 2 0 002 2M10 2h2v1.5a2 2 0 01-2 2" fill="none" stroke="#9aa3b4"/></svg>
    <svg width="14" height="14" viewBox="0 0 14 14" fill="none" stroke="#9aa3b4" stroke-width="1.5"><path d="M2.5 7a4.5 4.5 0 101.3-3.2L2 5.5"/><path d="M2 2v3.5h3.5M7 4.5V7l2 1.5"/></svg>
    <svg width="13" height="13" viewBox="0 0 13 13" fill="#9aa3b4"><circle cx="6.5" cy="3.5" r="3"/><path d="M1 13a5.5 4.5 0 0111 0z"/></svg>
  </nav>
</section>

<!-- Challenge overview -->
<section class="screen s3">
  <header class="app-header">
    <div class="avatar">TM</div>
    <div class="greet"><small>Welcome Back</small><strong>Theo M.</strong></div>
    <svg class="bell" width="16" height="18" viewBox="0 0 16 18" fill="none" stroke="#cfd4de" stroke-width="1.4"><path d="M3 13V8a5 5 0 0110 0v5l1.5 2h-13z"/><path d="M6.5 16.5a1.6 1.6 0 003 0"/></svg>
  </header>
  <div class="body">
    <div class="challenge">
      <span class="pill">Active</span>
      <div class="ch-title">100km Challenge</div>
      <div class="ch-sub">12 days remaining</div>
      <div class="prog-row"><span>35.8 km completed</span><span>53%</span></div>
      <div class="bar"><i></i></div>
      <div class="prize"><svg width="13" height="14" viewBox="0 0 13 14" fill="none" stroke="#5c8bff" stroke-width="1.6"><path d="M2 1l4.5 6L11 1"/><circle cx="6.5" cy="9.5" r="3.2"/></svg>Prize Pool<b>US. 10,000</b></div>
    </div>
    <div class="label">Recent Activities</div>
    <div class="activity"><div><strong>Today • 6:30 AM</strong><small>2.5 km &nbsp;22 min</small></div><svg width="7" height="10" viewBox="0 0 7 10" fill="none" stroke="#fff" stroke-width="1.8"><path d="M1.5 1l4 4-4 4"/></svg></div>
    <div class="activity"><div><strong>Yesterday • 6:15 AM</strong><small>3.2 km &nbsp;28 min</small></div><svg width="7" height="10" viewBox="0 0 7 10" fill="none" stroke="#fff" stroke-width="1.8"><path d="M1.5 1l4 4-4 4"/></svg></div>
    <div class="label">Past Challenges</div>
    <div class="past"><div><strong>50km Speed Run</strong><small>Completed • Won 2nd Place</small></div><div class="end"><svg width="11" height="14" viewBox="0 0 11 14" fill="none" stroke="var(--gold)" stroke-width="1.6"><circle cx="5.5" cy="5" r="3.6"/><path d="M3 8.5L2 13l3.5-1.5L9 13 8 8.5"/></svg></div></div>
    <div class="past"><div><strong>Marathon Prep</strong><small>Completed • Participation</small></div><div class="end"><svg width="11" height="14" viewBox="0 0 11 14" fill="none" stroke="#b8bfcc" stroke-width="1.6"><circle cx="5.5" cy="5" r="3.6"/><path d="M3 8.5L2 13l3.5-1.5L9 13 8 8.5"/></svg></div></div>
    <div class="btn" style="margin-top:16px">Start Run</div>
  </div>
  <nav class="tabbar">
    <svg width="14" height="13" viewBox="0 0 14 13" fill="var(--blue)"><path d="M7 1l6 5.5h-2V12H8.5V8.5h-3V12H3V6.5H1z"/></svg>
    <svg width="13" height="13" viewBox="0 0 13 13" fill="#9aa3b4"><path d="M3 1h7v4a3.5 3.5 0 01-7 0zM5.5 9h2v2h2v1.5h-6V11h2z"/><path d="M3 2H1v1.5a2 2 0 002 2M10 2h2v1.5a2 2 0 01-2 2" fill="none" stroke="#9aa3b4"/></svg>
    <svg width="14" height="14" viewBox="0 0 14 14" fill="none" stroke="#9aa3b4" stroke-width="1.5"><path d="M2.5 7a4.5 4.5 0 101.3-3.2L2 5.5"/><path d="M2 2v3.5h3.5M7 4.5V7l2 1.5"/></svg>
    <svg width="13" height="13" viewBox="0 0 13 13" fill="#9aa3b4"><circle cx="6.5" cy="3.5" r="3"/><path d="M1 13a5.5 4.5 0 0111 0z"/></svg>
  </nav>
</section>

<!-- Stats and past challenges -->
<section class="screen s4">
  <header class="app-header">
    <div class="avatar">TM</div>
    <div class="greet"><small>Welcome Back</small><strong>Theo M.</strong></div>
    <svg class="bell" width="16" height="18" viewBox="0 0 16 18" fill="none" stroke="#cfd4de" stroke-width="1.4"><path d="M3 13V8a5 5 0 0110 0v5l1.5 2h-13z"/><path d="M6.5 16.5a1.6 1.6 0 003 0"/></svg>
  </header>
  <div class="body">
    <div class="hero">
      <svg class="crown" width="16" height="12" viewBox="0 0 22 16" fill="none" stroke="var(--gold)" stroke-width="1.8"><path d="M2 4l5 5 4-7 4 7 5-5-2 9H4z"/><path d="M4 15h14"/></svg>
      <div style="font-size:9px;font-weight:500;margin-bottom:10px">Overall Statistics</div>
      <div class="stats">
        <div class="c"><svg width="12" height="13" viewBox="0 0 12 13" fill="none" stroke="#dbe3fb" stroke-width="1.2"><circle cx="6" cy="7.5" r="4.5"/><path d="M4.5 1h3M6 7.5V5"/></svg><span>Total Time</span><b>22 Min</b></div>
        <div class="c"><svg width="14" height="12" viewBox="0 0 14 12" fill="none" stroke="#dbe3fb" stroke-width="1.2"><path d="M1 10l4-4 2.5 2.5L13 3M9.5 3H13v3.5"/></svg><span>Pace</span><b>8'48" /km</b></div>
        <div class="c"><svg width="13" height="13" viewBox="0 0 13 13" fill="none" stroke="#dbe3fb" stroke-width="1.2"><path d="M3 1h7v4a3.5 3.5 0 01-7 0zM6.5 8.5V11M4 12h5M3 2H1v1.5a2 2 0 002 2M10 2h2v1.5a2 2 0 01-2 2"/></svg><span>Calories</span><b>186 kcal</b></div>
      </div>
    </div>
    <div class="label">Ongoing Challenge</div>
    <div class="challenge">
      <span class="pill">Active</span>
      <div class="ch-title">100km Challenge</div>
      <div class="ch-sub">12 days remaining</div>
      <div class="prog-row"><span>35.8 km completed</span><span>53%</span></div>
      <div class="bar"><i></i></div>
      <div class="prize"><svg width="13" height="14" viewBox="0 0 13 14" fill="none" stroke="#5c8bff" stroke-width="1.6"><path d="M2 1l4.5 6L11 1"/><circle cx="6.5" cy="9.5" r="3.2"/></svg>Prize Pool<b>US. 10,000</b></div>
    </div>
    <div class="label">Past Challenges</div>
    <div class="past"><div><strong>50km Speed Run</strong><small>▦ Oct 2023</small><small style="margin-top:4px">Completed • 2nd Place</small></div><div class="end"><svg width="11" height="14" viewBox="0 0 11 14" fill="none" stroke="var(--gold)" stroke-width="1.6"><circle cx="5.5" cy="5" r="3.6"/><path d="M3 8.5L2 13l3.5-1.5L9 13 8 8.5"/></svg><svg width="7" height="10" viewBox="0 0 7 10" fill="none" stroke="#fff" stroke-width="1.6"><path d="M1.5 1l4 4-4 4"/></svg></div></div>
    <div class="past"><div><strong>Marathon Prep</strong><small>▦ Sep 2023</small><small style="margin-top:4px">Completed • Participation</small></div><div class="end"><svg width="11" height="14" viewBox="0 0 11 14" fill="none" stroke="#b8bfcc" stroke-width="1.6"><circle cx="5.5" cy="5" r="3.6"/><path d="M3 8.5L2 13l3.5-1.5L9 13 8 8.5"/></svg><svg width="7" height="10" viewBox="0 0 7 10" fill="none" stroke="#fff" stroke-width="1.6"><path d="M1.5 1l4 4-4 4"/></svg></div></div>
    <div class="past" style="height:26px;overflow:hidden;align-items:flex-start"><div><strong>Summer Run</strong><small>▦ Aug 2023</small></div><div class="end"><svg width="11" height="14" viewBox="0 0 11 14" fill="none" stroke="#5c8bff" stroke-width="1.6"><circle cx="5.5" cy="5" r="3.6"/><path d="M3 8.5L2 13l3.5-1.5L9 13 8 8.5"/></svg></div></div>
  </div>
  <nav class="tabbar" style="padding-top:8px">
    <svg width="14" height="13" viewBox="0 0 14 13" fill="#9aa3b4"><path d="M7 1l6 5.5h-2V12H8.5V8.5h-3V12H3V6.5H1z"/></svg>
    <svg width="13" height="13" viewBox="0 0 13 13" fill="var(--blue)"><path d="M3 1h7v4a3.5 3.5 0 01-7 0zM5.5 9h2v2h2v1.5h-6V11h2z"/><path d="M3 2H1v1.5a2 2 0 002 2M10 2h2v1.5a2 2 0 01-2 2" fill="none" stroke="var(--blue)"/></svg>
    <svg width="14" height="14" viewBox="0 0 14 14" fill="none" stroke="#9aa3b4" stroke-width="1.5"><path d="M2.5 7a4.5 4.5 0 101.3-3.2L2 5.5"/><path d="M2 2v3.5h3.5M7 4.5V7l2 1.5"/></svg>
    <svg width="13" height="13" viewBox="0 0 13 13" fill="#9aa3b4"><circle cx="6.5" cy="3.5" r="3"/><path d="M1 13a5.5 4.5 0 0111 0z"/></svg>
  </nav>
</section>

<!-- Challenge detail -->
<section class="screen s5">
  <header class="topbar">
    <svg width="13" height="11" viewBox="0 0 13 11" fill="none" stroke="#fff" stroke-width="1.8"><path d="M12 5.5H2M6 1L1.5 5.5 6 10"/></svg>Ongoing Challenge
  </header>
  <div class="detail-hero">
    <div class="live"><i></i>Active Challenge</div>
    <h2>100km Challenge</h2>
  </div>
  <div class="tiles">
    <div class="tile"><svg width="14" height="9" viewBox="0 0 14 9" fill="#6d95ff"><circle cx="4" cy="2.5" r="2"/><circle cx="10" cy="2.5" r="2"/><path d="M0 9a4 3.5 0 018 0zM6 9a4 3.5 0 018 0z"/></svg><div>Players</div><b>2,458</b></div>
    <div class="tile"><svg width="9" height="9" viewBox="0 0 9 9"><circle cx="4.5" cy="4.5" r="4.5" fill="var(--bronze)"/><path d="M4.5 2v2.7h2" stroke="#1b2437" fill="none"/></svg><div>Days Left</div><b>12</b></div>
    <div class="tile"><svg width="12" height="10" viewBox="0 0 13 13" fill="var(--gold)"><path d="M3 1h7v4a3.5 3.5 0 01-7 0zM5.5 9h2v2h2v1.5h-6V11h2z"/></svg><div>Prize</div><b>$10,000</b></div>
  </div>
  <div class="panel">
    <h3>Your Progress</h3>
    <div class="ch-sub" style="margin-top:3px">35.8 km completed</div>
    <div class="bar"><i></i></div>
    <div class="stats" style="margin-top:10px;color:#d6dbe4"><div><span style="color:#c6ccd8">Time</span><b>48.5h</b></div><div class="c"><span style="color:#c6ccd8">Speed</span><b>8.5km/h</b></div><div class="c"><span style="color:#c6ccd8">Rank</span><b>#234</b></div></div>
  </div>
  <div class="sec">Your Progress</div>
  <div class="panel rules">
    <div class="rule"><svg width="14" height="12" viewBox="0 0 14 12" fill="none" stroke="#cfd4de" stroke-width="1.2"><path d="M1 10l4-4 2.5 2.5L13 3M9.5 3H13v3.5"/></svg><div><strong>Complete 100km</strong><small>Complete 100km Within challenge period</small></div></div>
    <div class="rule"><svg width="13" height="13" viewBox="0 0 13 13" fill="none" stroke="#cfd4de" stroke-width="1.2"><rect x="1" y="2.5" width="11" height="9.5" rx="1"/><path d="M1 5.5h11M4 1v3M9 1v3"/></svg><div><strong>30 Days Timeline</strong><small>Ends Dec 20, 2024</small></div></div>
    <div class="rule"><svg width="13" height="14" viewBox="0 0 12 13" fill="none" stroke="#cfd4de" stroke-width="1.2"><circle cx="6" cy="7.5" r="4.5"/><path d="M4.5 1h3M6 7.5V5"/></svg><div><strong>Minimum 2km per run</strong><small>Each activity must qualify</small></div></div>
  </div>
  <div class="sec">Prize Distribution</div>
  <div class="places">
    <div class="place"><svg width="11" height="14" viewBox="0 0 11 14" fill="none" stroke="var(--gold)" stroke-width="1.6"><circle cx="5.5" cy="5" r="3.6"/><path d="M3 8.5L2 13l3.5-1.5L9 13 8 8.5"/></svg>1st Place<b>$5,000</b></div>
    <div class="place"><svg width="11" height="14" viewBox="0 0 11 14" fill="none" stroke="#dfe3ea" stroke-width="1.6"><circle cx="5.5" cy="5" r="3.6"/><path d="M3 8.5L2 13l3.5-1.5L9 13 8 8.5"/></svg>2nd Place<b>$3,000</b></div>
    <div class="place"><svg width="11" height="14" viewBox="0 0 11 14" fill="none" stroke="var(--bronze)" stroke-width="1.6"><circle cx="5.5" cy="5" r="3.6"/><path d="M3 8.5L2 13l3.5-1.5L9 13 8 8.5"/></svg>3rd Place<b>$2,000</b></div>
  </div>
  <div class="btn" style="margin:0 12px;position:relative;top:-6px">Join Challenge</div>
</section>

<!-- Admin: create challenge -->
<section class="screen s6">
  <header class="topbar">
    <svg width="13" height="11" viewBox="0 0 13 11" fill="none" stroke="#fff" stroke-width="1.8"><path d="M12 5.5H2M6 1L1.5 5.5 6 10"/></svg>Create Challenge
    <span class="save">Save</span>
  </header>
  <div class="form">
    <label>Your Progress</label><div class="field">ex 108 km Challenge</div>
    <label>Description</label><div class="field" style="height:66px;align-items:flex-start;padding-top:10px">Description your Challenge</div>
    <label>Upload Banner</label><div class="dashed">Click to upload banner image<small>Recommended: 1200 x 400px</small></div>
    <label>Challenge Duration</label><div class="field">Start Date / End Date</div>
    <label>Challenge Rules</label>
    <div class="field">Enter Rule<svg style="margin-left:auto" width="11" height="12" viewBox="0 0 11 12" fill="none" stroke="#8e97aa" stroke-width="1.2"><path d="M1 2.5h9M4 2.5V1h3v1.5M2 2.5l.7 9h5.6l.7-9M4.3 4.5v5M6.7 4.5v5"/></svg></div>
    <div class="field" style="margin-top:5px;border-style:dashed;background:none;justify-content:center">+ Add Rule</div>
  </div>
  <div class="btn" style="margin:16px 14px 0">Publish Challenge</div>
</section>

</body>
</html>
```